Poster Design Project - Lebanese Food Cooking Classes

A poster which will be used for multiple announcements of cooking classes called “Hidden Hearth Kitchen Journeys”.

The poster will be used for an interactive cooking course. The participant will: Discover the healthy, delicious and unexpected cuisine of Lebanon. Learn surprising techniques to create apparently complex dishes. Eye appeal is important and spices are crucial. Have an experience of true Middle Eastern hospitality.

I think the poster could have colorful spices, wooden utensils and a distinctive feel of the celebration of the simple, yet sophisticated, foods that are the inspiration for all Middle Eastern cuisine, where the table is the canvas and the food and its garnish is the art.

I would like the following language on the poster: Hidden Hearth Kitchen Journeys, an interactive course. Create,Taste, Experience 

The specific detail for the course offering to place in the blank space area is the following:

Brellowmere Institution
Week 8
August 13-16, 2012

I will require the layered PSD, or AI files. 

Target Market(s)

Sophisticated and open to new food and flavor experiences

Industry/Entity Type

Cooking

Requirements
Must have
• A space somewhere appropriate in the poster where the detail of the course offer can be printed.
Nice to have

• The feel of orange, yellow, red and green spice colors, lemons, olives, parsley, grapes, apricots, figs, olive oil.

Should not have
• Should not have mountains of Lebanon, camels, or the Lebanese flag, or cedar trees, or old ladies bent over a wood stove or anyone else.

```html
<!DOCTYPE html>
<html lang="en">
<head>
<meta charset="utf-8">
<title>Hidden Hearth Kitchen Journeys – Poster</title>
<link rel="stylesheet" href="https://fonts.googleapis.com/css2?family=Righteous&family=Cinzel:wght@600;700&display=swap">
<style>
  :root {
    --page-top: #ffffff;
    --page-bottom: #86b4c8;
    --poster-white: #ffffff;
    --green-deep: #2f8f2a;
    --green-mid: #5fb534;
    --green-light: #b9dd3c;
    --title-orange: #f7a21b;
    --title-gold: #ffd23a;
    --title-edge: #c0461a;
    --course-red: #e0451f;
    --band-text: #ffffff;
  }
  * { box-sizing: border-box; margin: 0; padding: 0; }
  html, body { width: 1200px; height: 800px; overflow: hidden; }
  body {
    background: linear-gradient(160deg, var(--page-top) 0%, #dde9ef 40%, var(--page-bottom) 100%);
    position: relative;
  }
  .poster {
    position: absolute;
    left: 331px; top: 20px;
    width: 539px; height: 760px;
    background: var(--poster-white);
    box-shadow: 0 2px 8px rgba(0,0,0,.18);
    overflow: hidden;
  }
  .top-swoosh { position: absolute; left: 0; top: 0; width: 539px; height: 170px; }
  .title {
    position: absolute; left: 0; width: 100%;
    text-align: center;
    font-family: "Righteous", sans-serif;
    text-transform: uppercase;
    color: var(--title-orange);
    background: linear-gradient(180deg, var(--title-gold), var(--title-orange) 60%, #e8741a);
    -webkit-background-clip: text; background-clip: text;
    -webkit-text-fill-color: transparent;
    filter: drop-shadow(1px 1px 0 var(--title-edge)) drop-shadow(-1px -1px 0 var(--title-edge)) drop-shadow(2px 3px 2px rgba(0,0,0,.35));
  }
  .title-main { top: 52px; font-size: 46px; letter-spacing: 1px; line-height: 1; }
  .title-sub { top: 114px; font-size: 25px; letter-spacing: 1px; line-height: 1; }
  .course-type {
    position: absolute; top: 180px; left: 0; width: 100%;
    text-align: center;
    font-family: "Cinzel", serif; font-weight: 600;
    font-size: 18px; letter-spacing: 1px;
    color: var(--course-red);
  }
  .dish-photo {
    position: absolute; left: 0; top: 220px;
    width: 539px; height: 408px;
    background:
      radial-gradient(ellipse at 55% 60%, #c9a070 0%, #9c7a55 22%, rgba(255,255,255,0) 45%),
      radial-gradient(ellipse at 70% 40%, #e8622a 0%, rgba(255,255,255,0) 25%),
      radial-gradient(ellipse at 20% 55%, #7fb53a 0%, rgba(255,255,255,0) 22%),
      linear-gradient(180deg, #f4efe6 0%, #ffffff 50%, #f1f1ec 100%);
  }
  .tagline {
    position: absolute; top: 640px; left: 0; width: 100%;
    text-align: center;
    font-size: 25px; letter-spacing: 1px;
  }
  .details-band {
    position: absolute; left: 0; bottom: 0;
    width: 539px; height: 89px;
    background: linear-gradient(90deg, var(--green-deep) 0%, var(--green-mid) 50%, var(--green-light) 100%);
    display: flex; flex-direction: column; align-items: center; justify-content: center;
    font-family: "Cinzel", serif; font-weight: 700;
    color: var(--band-text);
    font-size: 16px; line-height: 21px; letter-spacing: .5px;
    text-align: center;
  }
</style>
</head>
<body>
  <main class="poster">
    <svg class="top-swoosh" viewBox="0 0 539 170" aria-hidden="true">
      <defs>
        <linearGradient id="swoosh-green" x1="0" y1="0" x2="1" y2="0">
          <stop offset="0" stop-color="#2e8f2b"/>
          <stop offset=".55" stop-color="#62b836"/>
          <stop offset="1" stop-color="#a8d63a"/>
        </linearGradient>
      </defs>
      <path d="M0 0 H539 V92 C420 62 300 95 180 130 C110 150 50 158 0 152 Z" fill="url(#swoosh-green)"/>
      <path d="M0 140 C60 146 120 132 190 112 C300 80 420 52 539 78 V86 C420 60 300 88 190 120 C120 140 60 152 0 148 Z" fill="#c9e86a" opacity=".7"/>
      <path d="M0 40 C150 20 350 10 539 30" stroke="#7fc84a" stroke-width="10" fill="none" opacity=".35"/>
    </svg>

    <h1 class="title title-main">Hidden Hearth</h1>
    <p class="title title-sub">Kitchen Journeys</p>
    <p class="course-type">AN INTERACTIVE COURSE</p>

    <div class="dish-photo" role="img" aria-label="Photograph of a grilled whole fish with lime, fresh salad and crayfish on a white plate, framed by an orange, red and green swirl border"></div>

    <p class="title tagline">Create -Taste- Experience</p>

    <footer class="details-band">
      <span>Brellowmere Institution</span>
      <span>Week 8</span>
      <span>August 13-16, 2012</span>
    </footer>
  </main>
</body>
</html>
```